Butcher shop

We have 2 butcher shops:

Shop 9, Ridgeway Court, Aberdeen NSW 2336
Ph 02 6512 3840

47 Marlow St, Scone NSW 2337
Ph 02 6518 2274

ABN 48 907 215 816

I would like this info on reverse of card and my personal info on front of card. I have a logo I would like to use also. Require a very smooth thick matte card, with colour both sides.

Front of card should say:

Linda Farrugia
Accounts

Ph 0437 620 915
E lindafarrugia@quollmail.com.au

Industry/Entity Type

Shop

Contact Information for Business Card

Linda Farrugia
Ph 0437 620 915

Logo Text

Farrugia's Quality Meats

Logo styles of interest
Pictorial/Combination Logo
Requirements
Must have
• We use Century Gothic Font

```html
<!DOCTYPE html>
<html lang="en">
<head>
<meta charset="utf-8">
<title>Farrugia's Quality Meats – Business Cards</title>
<link rel="stylesheet" href="https://fonts.googleapis.com/css2?family=Questrial&display=swap">
<style>
  :root {
    --backdrop: #e4e1dc;
    --card-blue: #a9dcef;
    --band-blue: #c6e9f5;
    --ink: #1c1c1c;
    --shadow: rgba(0, 0, 0, 0.14);
  }
  * { box-sizing: border-box; margin: 0; padding: 0; }
  html, body {
    width: 1200px;
    height: 960px;
    overflow: hidden;
    background: var(--backdrop);
  }
  .sheet {
    width: 1200px;
    height: 960px;
    display: flex;
    flex-direction: column;
    align-items: center;
    justify-content: center;
    gap: 36px;
    font-family: "Questrial", "Century Gothic", sans-serif;
    color: var(--ink);
  }
  .card {
    position: relative;
    width: 720px;
    height: 411px;
    background: var(--card-blue);
    box-shadow: 0 6px 18px var(--shadow);
    overflow: hidden;
  }
  .card__band {
    position: absolute;
    left: 0;
    right: 0;
    bottom: 0;
    height: 62px;
    background: var(--band-blue);
  }

  /* Personal side */
  .contact {
    position: absolute;
    left: 52px;
    top: 54px;
    font-size: 17px;
    line-height: 1.45;
  }
  .contact__name { font-size: 22px; margin-bottom: 2px; }
  .contact__role { margin-bottom: 14px; }
  .contact__label { display: inline-block; width: 32px; }

  .mini-logo {
    position: absolute;
    right: 44px;
    top: 44px;
    font-size: 15px;
    line-height: 1.15;
  }

  /* Brand side */
  .brand {
    position: absolute;
    left: 0;
    right: 0;
    top: 56px;
    display: flex;
    flex-direction: column;
    align-items: center;
    gap: 14px;
  }
  .brand__mark {
    width: 40px;
    height: 40px;
    background: var(--ink);
  }
  .brand__name {
    font-size: 40px;
    line-height: 1.08;
    text-align: center;
  }
  .shops {
    position: absolute;
    left: 0;
    right: 0;
    top: 250px;
    display: flex;
    justify-content: center;
    gap: 56px;
    font-size: 14px;
    line-height: 1.45;
  }
  .shop { text-align: center; }
  .abn {
    position: absolute;
    left: 0;
    right: 0;
    bottom: 0;
    height: 62px;
    display: flex;
    align-items: center;
    justify-content: center;
    font-size: 14px;
    letter-spacing: 0.04em;
  }
</style>
</head>
<body>
  <main class="sheet">
    <section class="card card--personal" aria-label="Card front: personal details">
      <div class="contact">
        <p class="contact__name">Linda Farrugia</p>
        <p class="contact__role">Accounts</p>
        <p><span class="contact__label">Ph</span>0437 620 915</p>
        <p><span class="contact__label">E</span>lindafarrugia@quollmail.com.au</p>
      </div>
      <p class="mini-logo">Farrugia's<br>Quality Meats</p>
      <div class="card__band"></div>
    </section>

    <section class="card card--brand" aria-label="Card back: shop details">
      <div class="brand">
        <span class="brand__mark" aria-hidden="true"></span>
        <p class="brand__name">Farrugia's<br>Quality Meats</p>
      </div>
      <div class="shops">
        <address class="shop" style="font-style: normal;">
          Shop 9, Ridgeway Court<br>Aberdeen NSW 2336<br>Ph 02 6512 3840
        </address>
        <address class="shop" style="font-style: normal;">
          47 Marlow St<br>Scone NSW 2337<br>Ph 02 6518 2274
        </address>
      </div>
      <div class="card__band"></div>
      <p class="abn">ABN 48 907 215 816</p>
    </section>
  </main>
</body>
</html>
```